Backflow Prevention Test Gauge Calibration Service

Our company, Northfield Valve Supply Company, specializes in backflow prevention, a backflow preventer is a valve on the public drinking water system that prevents contamination. Backflow preventers need to be tested annually using a backflow test gauge. A backflow test gauge is considered an instrument and is required to be tested and calibrated annually to ensure they are working accurately. We offer that service, along with repair services if the instrument is damaged, and we refer to it as a "Hassle Free" service. We schedule the service for them once they provide their information and then email them a shipping label that they can print out, tape on their box and send the package from their business or home. We have a quick-turnaround time for this service because we understand how important this piece of equipment is for our customers to continue their job.

The main points we want to highlight on the flyer are:
* Hassle free shipping
* 1-Day turnaround time
* Service all gauge models
* Price includes incoming & return freight
* Honor all manufacturer warranties

We would like to include the manufacturers' logos and photos of the gauges that our customers use and will recognize (photos in brief).

There are two ways to schedule this service with us. They can call us at (800) 642-3871 or they can fill out a form on our website www.pipeguardshop.com.

Our text preferences are Myriad Pro and Tahoma. Our brand colors are red, white and blue. Please visit our website to get an idea of our style too.

```html
<!DOCTYPE html>
<html lang="en">
<head>
<meta charset="utf-8">
<title>Backflow Prevention Test Gauge Calibration Service</title>
<link href="https://fonts.googleapis.com/css2?family=PT+Sans:wght@400;700&family=Source+Sans+3:wght@400;600;700&display=swap" rel="stylesheet">
<style>
  :root{
    --blue:#1b4f9c;
    --blue-deep:#213a86;
    --navy:#0b1450;
    --red:#e8283a;
    --white:#ffffff;
    --ink:#1f1f1f;
    --rule:#9aa3b5;
    --photo-a:#b9a37a;
    --photo-b:#5b6a4a;
    --gear-a:#d9dce2;
    --gear-b:#7d8593;
  }
  html,body{margin:0;padding:0;overflow:hidden;background:#e6e6e6;}
  .flyer{position:relative;width:945px;height:1200px;overflow:hidden;background:var(--white);font-family:"Source Sans 3",sans-serif;}
  .flyer-shapes{position:absolute;inset:0;}
  .brand{position:absolute;left:434px;top:44px;display:flex;align-items:center;gap:14px;color:var(--blue);}
  .brand-dot{width:48px;height:48px;border-radius:50%;background:var(--blue);flex:none;}
  .brand-name{font-weight:400;font-size:30px;line-height:31px;}
  .brand-name span{display:block;}
  .headline{position:absolute;left:470px;top:174px;margin:0;color:var(--white);font-weight:700;font-size:51px;line-height:49.5px;letter-spacing:-.6px;text-shadow:2px 3px 4px rgba(0,0,0,.35);}
  .intro{position:absolute;left:475px;top:383px;width:436px;margin:0;color:var(--white);font-weight:600;font-size:18.5px;line-height:22.9px;}
  .why-title{position:absolute;left:57px;top:801px;margin:0;color:var(--white);font-family:"PT Sans",sans-serif;font-weight:700;font-size:21px;line-height:32px;}
  .benefits{position:absolute;left:42px;top:848px;margin:0;padding:0;list-style:none;}
  .benefit{display:flex;align-items:center;height:40px;}
  .benefit-icon{width:30px;height:30px;margin-right:21px;flex:none;}
  .benefit-text{color:var(--blue);font-family:"PT Sans",sans-serif;font-weight:700;font-size:21px;letter-spacing:.6px;border-bottom:1px solid var(--rule);padding:6px 0 5px;min-width:315px;}
  .benefit:last-child .benefit-text{border-bottom:none;}
  .makers{position:absolute;left:42px;top:1088px;display:flex;align-items:center;color:var(--ink);font-family:"Source Sans 3",sans-serif;font-weight:700;font-size:22px;}
  .maker{padding:0 14px;border-left:1px solid var(--rule);line-height:34px;}
  .maker:first-child{padding-left:0;border-left:none;}
  .schedule-bar{position:absolute;left:0;top:1134px;width:945px;height:66px;background:var(--blue);}
  .schedule-text{position:absolute;left:46px;top:1141px;margin:0;color:var(--white);font-family:"PT Sans",sans-serif;font-weight:700;line-height:24px;}
  .schedule-text .lead{display:block;font-size:19px;}
  .schedule-text .strong{display:block;font-size:22px;}
  .contact{position:absolute;left:593px;top:1116px;width:352px;height:84px;background:var(--red);border-top-left-radius:22px;color:var(--white);text-align:center;font-family:"PT Sans",sans-serif;font-weight:700;}
  .contact-phone{display:block;margin-top:12px;font-size:31px;line-height:34px;}
  .contact-web{display:block;font-size:23px;line-height:27px;}
</style>
</head>
<body>
<div class="flyer">
  <svg class="flyer-shapes" width="945" height="1200" viewBox="0 0 945 1200">
    <defs>
      <linearGradient id="photoTone" x1="0" y1="0" x2="1" y2="1">
        <stop offset="0" stop-color="var(--photo-b)"/>
        <stop offset=".55" stop-color="var(--photo-a)"/>
        <stop offset="1" stop-color="#d8c49a"/>
      </linearGradient>
      <linearGradient id="panelTone" x1="0" y1="0" x2="1" y2="0">
        <stop offset="0" stop-color="var(--blue)"/>
        <stop offset="1" stop-color="var(--blue-deep)"/>
      </linearGradient>
      <linearGradient id="foldTone" x1="0" y1="0" x2="1" y2="1">
        <stop offset="0" stop-color="var(--blue-deep)"/>
        <stop offset=".6" stop-color="var(--navy)"/>
      </linearGradient>
      <radialGradient id="gearTone">
        <stop offset="0" stop-color="var(--gear-a)"/>
        <stop offset="1" stop-color="var(--gear-b)"/>
      </radialGradient>
    </defs>

    <path role="img" aria-label="Photo of a technician calibrating a backflow test gauge at a workbench"
          d="M0,0 H282 C318,95 390,140 500,145 L583,145 V680 H470 C300,690 120,640 0,478 Z" fill="url(#photoTone)"/>

    <path class="panel-fold" d="M433,586 C480,590 540,596 583,600 V676 Z" fill="url(#foldTone)"/>
    <path class="title-panel" d="M433,144 C630,135 860,210 945,310 V830 C900,760 860,650 760,605 C700,598 640,600 583,598 C540,592 480,588 433,586 Z" fill="url(#panelTone)"/>

    <g class="gauge-badge">
      <circle cx="287" cy="680" r="104" fill="var(--white)"/>
      <path d="M191,680 A96,96 0 0 1 383,680" fill="none" stroke="var(--blue)" stroke-width="7"/>
      <path d="M191,680 A96,96 0 0 0 383,680" fill="none" stroke="var(--red)" stroke-width="7"/>
      <circle role="img" aria-label="Product photo of an analog backflow test gauge with hoses" cx="287" cy="680" r="80" fill="url(#gearTone)"/>
    </g>
    <g class="gauge-badge">
      <circle cx="763" cy="703" r="148" fill="var(--white)"/>
      <path d="M625,703 A138,138 0 0 1 901,703" fill="none" stroke="var(--blue)" stroke-width="8"/>
      <path d="M625,703 A138,138 0 0 0 901,703" fill="none" stroke="var(--red)" stroke-width="8"/>
      <circle role="img" aria-label="Product photo of a cased dial test gauge kit with colored hoses" cx="763" cy="703" r="118" fill="url(#gearTone)"/>
    </g>
    <g class="gauge-badge">
      <circle cx="502" cy="820" r="125" fill="var(--white)"/>
      <path d="M385,820 A117,117 0 0 1 619,820" fill="none" stroke="var(--blue)" stroke-width="8"/>
      <path d="M385,820 A117,117 0 0 0 619,820" fill="none" stroke="var(--red)" stroke-width="8"/>
      <circle role="img" aria-label="Product photo of a hand holding a digital backflow test gauge" cx="502" cy="820" r="100" fill="url(#gearTone)"/>
    </g>

    <rect role="img" aria-label="Product photo of a test kit toolbox with gauge and colored hoses"
          x="626" y="862" width="284" height="216" rx="30" fill="url(#gearTone)"/>

    <path class="why-banner" d="M45,801 H318 L343,833 H45 Z" fill="var(--red)"/>
    <path d="M45,801 H308 L320,833 H45 Z" fill="var(--blue)"/>
  </svg>

  <div class="brand">
    <span class="brand-dot"></span>
    <div class="brand-name"><span>Northfield Valve</span><span>Supply Company</span></div>
  </div>

  <h1 class="headline">Backflow<br>Prevention<br>Test Gauge<br>Calibration Service</h1>

  <p class="intro">We specializes in backflow prevention, a backflow preventer is a valve on the public drinking water system that prevents contamination. Backflow preventers need to be tested annually using a backflow test gauge. A backflow test gauge is considered an instrument and is required to be tested and calibrated annually to ensure they are working accurately.</p>

  <h2 class="why-title">WHY CHOOSE US</h2>

  <ul class="benefits">
    <li class="benefit">
      <svg class="benefit-icon" viewBox="0 0 30 30"><rect x="2" y="7" width="15" height="13" fill="var(--red)"/><path d="M17,11 H23 L28,16 V21 H17 Z" fill="none" stroke="var(--blue)" stroke-width="2"/><circle cx="8" cy="22" r="3" fill="var(--blue)"/><circle cx="23" cy="22" r="3" fill="var(--blue)"/></svg>
      <span class="benefit-text">HASSLE FREE SHIPPING</span>
    </li>
    <li class="benefit">
      <svg class="benefit-icon" viewBox="0 0 30 30"><circle cx="15" cy="15" r="12" fill="none" stroke="var(--blue)" stroke-width="2.5"/><text x="15" y="19" text-anchor="middle" font-family="PT Sans, sans-serif" font-weight="700" font-size="11" fill="var(--red)">24</text></svg>
      <span class="benefit-text">1-DAY TURNAROUND TIME</span>
    </li>
    <li class="benefit">
      <svg class="benefit-icon" viewBox="0 0 30 30"><circle cx="15" cy="15" r="12" fill="none" stroke="var(--blue)" stroke-width="3" stroke-dasharray="4 2"/><circle cx="15" cy="15" r="7" fill="none" stroke="var(--red)" stroke-width="2"/><path d="M15,15 L19,11" stroke="var(--red)" stroke-width="2"/></svg>
      <span class="benefit-text">SERVICE ALL GAUGE MODELS</span>
    </li>
    <li class="benefit">
      <svg class="benefit-icon" viewBox="0 0 30 30"><path d="M8,5 H26 V22 H8 Z" fill="none" stroke="var(--blue)" stroke-width="2.5"/><path d="M14,5 V12 H20 V5" fill="var(--blue)"/><path d="M3,18 A7,7 0 0 0 10,26" fill="none" stroke="var(--red)" stroke-width="2"/></svg>
      <span class="benefit-text">PRICE INCLUDES INCOMING &amp; RETURN FREIGHT</span>
    </li>
    <li class="benefit">
      <svg class="benefit-icon" viewBox="0 0 30 30"><circle cx="15" cy="12" r="9" fill="none" stroke="var(--blue)" stroke-width="2.5"/><path d="M11,12 L14,15 L19,9" fill="none" stroke="var(--red)" stroke-width="2.5"/><path d="M10,20 L8,28 L12,26 L14,29 M20,20 L22,28 L18,26 L16,29" fill="none" stroke="var(--blue)" stroke-width="2"/></svg>
      <span class="benefit-text">HONOR ALL MANUFACTURER WARRANTIES</span>
    </li>
  </ul>

  <div class="makers">
    <span class="maker">Halden</span>
    <span class="maker">Corvo</span>
    <span class="maker">Plainsway Instrument</span>
    <span class="maker">Brightline</span>
  </div>

  <div class="schedule-bar"></div>
  <p class="schedule-text">
    <span class="lead">TWO WAYS TO SCHEDULE THIS SERVICE WITH US.</span>
    <span class="strong">CALL US OR FILL OUT A FORM ON OUR WEBSITE</span>
  </p>

  <div class="contact">
    <span class="contact-phone">(800) 642-3871</span>
    <span class="contact-web">www.pipeguardshop.com</span>
  </div>
</div>
</body>
</html>
```